Marlow Presents Box

Marlow Presents is a new company selling Experience Gifts. We want to create a unique gift pack that will be sent to the gift recipient containing information about the chosen experience.
We have selected a box style (see movie attached). The exact size of the box is:
Width: 16.2 cm
Height: 3,81 cm
Length: 23.8 cm
Our logo and strapline are attached. We hope to use the words 'Experiences Revealed' (our slogan) in a creative way on the packaging or as part of the box opening experience. We prefer something minimalist, clever - black is our preferred packaging color. But we are open to suggestions. We can print directly onto the box. We can also add a seal, stickers, a sleeve or any other graphic addition that would create a premium box and make receiving this gift pack a memorable moment.
Look and feel
Each slider illustrates characteristics of the customer's brand and the style your logo design should communicate.

```html
<!DOCTYPE html>
<html lang="en">
<head>
<meta charset="utf-8">
<title>Marlow Presents – Box Lid Artwork</title>
<link href="https://fonts.googleapis.com/css2?family=Montserrat:wght@400;700;800&display=swap" rel="stylesheet">
<style>
  :root {
    --paper: #ffffff;
    --box-black: #222222;
    --signal-red: #ed1c24;
    --fold-guide: #8a1418;
    --ink: #000000;
    --logo-white: #ffffff;
  }
  html, body {
    margin: 0;
    padding: 0;
    width: 1200px;
    height: 1003px;
    overflow: hidden;
    background: var(--paper);
  }
  .artboard {
    display: block;
    width: 1200px;
    height: 1003px;
  }
  .dimension-label {
    font-family: "Montserrat", sans-serif;
    font-weight: 700;
    font-size: 19px;
    fill: var(--ink);
  }
  .lid-base { fill: var(--box-black); }
  .accent-band { fill: var(--signal-red); }
  .fold-guide {
    fill: none;
    stroke: var(--fold-guide);
    stroke-width: 0.8;
  }
  .brand-name {
    font-family: "Montserrat", sans-serif;
    font-weight: 800;
    fill: var(--logo-white);
  }
  .slogan {
    font-family: "Montserrat", sans-serif;
    font-weight: 400;
    font-size: 41px;
    fill: var(--logo-white);
  }
</style>
</head>
<body>
<svg class="artboard" viewBox="0 0 1200 1003" xmlns="http://www.w3.org/2000/svg">
  <text class="dimension-label" x="623" y="134" text-anchor="middle">23.8 cm</text>
  <text class="dimension-label" x="0" y="0" text-anchor="middle" transform="translate(115 514) rotate(-90)">16.2 cm</text>
  <text class="dimension-label" x="198" y="906" text-anchor="middle">3,81 cm</text>

  <g class="box-lid">
    <rect class="lid-base" x="136" y="158" width="943" height="712"/>
    <polygon class="accent-band" points="771,158 1079,158 1079,582"/>
    <polygon class="accent-band" points="136,467 136,870 427,870"/>

    <g class="fold-guides">
      <line class="fold-guide" x1="253" y1="158" x2="253" y2="870"/>
      <line class="fold-guide" x1="964" y1="158" x2="964" y2="870"/>
      <line class="fold-guide" x1="139" y1="272" x2="1079" y2="272"/>
      <line class="fold-guide" x1="136" y1="756" x2="1079" y2="756"/>
      <line class="fold-guide" x1="139" y1="272" x2="139" y2="756"/>
      <line class="fold-guide" x1="1078" y1="582" x2="1078" y2="756"/>
      <line class="fold-guide" x1="253" y1="158" x2="771" y2="158"/>
      <line class="fold-guide" x1="253" y1="870" x2="427" y2="870"/>
    </g>

    <g class="brand-lockup">
      <text class="brand-name" x="363" y="487" font-size="192" textLength="464" lengthAdjust="spacingAndGlyphs">MARLOW</text>
      <text class="brand-name" x="363" y="648" font-size="205" textLength="464" lengthAdjust="spacingAndGlyphs">PRESENTS</text>
      <text class="slogan" x="373" y="701" textLength="454" lengthAdjust="spacingAndGlyphs">Experiences Revealed</text>
    </g>
  </g>
</svg>
</body>
</html>
```